Where Did The Oddness Start Podcast Design

I'm starting a new podcast called, "Where did the oddness start?" It highlights bizarre and often unintentional record holders, wannabe record holders and should be record holders. I'm looking for a design that incorporates the title and appears a little off kilter like the show and stir curiosity. Leaninsstoward some autumn colors; burnt rsd and some type of gold but open to other colors.sPodcast art specs:sCover art must be in the JPEG or PNG file formats and in the RGB color space with a minimum size of 1400 x 1400 pixels and a maximum size of 3000 x 3000 pixelss

```html
<!DOCTYPE html>
<html lang="en">
<head>
<meta charset="utf-8">
<title>Where Did The Oddness Start? – Podcast Cover</title>
<link rel="stylesheet" href="https://fonts.googleapis.com/css2?family=League+Spartan:wght@800&display=swap">
<style>
  :root {
    --bg-deep: #241212;
    --bg-warm: #2f1515;
    --gold: #f68b1f;
  }
  html, body {
    margin: 0;
    padding: 0;
    width: 1200px;
    height: 1200px;
    overflow: hidden;
    background: var(--bg-deep);
  }
  .cover {
    display: block;
    width: 1200px;
    height: 1200px;
  }
  .show-name {
    font-family: "League Spartan", "Montserrat", sans-serif;
    font-weight: 800;
    fill: var(--gold);
    text-anchor: middle;
  }
  .show-name__line--top { font-size: 150px; }
  .show-name__line--middle { font-size: 300px; }
  .show-name__line--bottom { font-size: 210px; }
</style>
</head>
<body>
<svg class="cover" viewBox="0 0 1200 1200" xmlns="http://www.w3.org/2000/svg" aria-labelledby="cover-title">
  <title id="cover-title">Where did the oddness start?</title>
  <defs>
    <radialGradient id="backdrop" cx="50%" cy="45%" r="75%">
      <stop offset="0" stop-color="var(--bg-warm)"/>
      <stop offset="1" stop-color="var(--bg-deep)"/>
    </radialGradient>
  </defs>

  <rect class="backdrop" width="1200" height="1200" fill="url(#backdrop)"/>

  <g class="show-name">
    <text class="show-name__line show-name__line--top" x="600" y="320" textLength="1060" lengthAdjust="spacingAndGlyphs">WHERE DID THE</text>
    <text class="show-name__line show-name__line--middle" x="600" y="720" textLength="1060" lengthAdjust="spacingAndGlyphs">ODDNESS</text>
    <text class="show-name__line show-name__line--bottom" x="600" y="995" textLength="1000" lengthAdjust="spacingAndGlyphs">START?</text>
  </g>
</svg>
</body>
</html>
```